Web Site Redesign

We operate a data centre facility specialing in colocation and Fibre optic connectivity (i.e. point to point fibre services and internet over fibre).

We have an existing site located at www.corvanlink.example however this is very very tired and requires a redesign. We are looking for a fresh new design that will be appealing to potential customers.

The Company name is Corvan Lk and the primary corporate colour is bright red with secondary colours of white, grey and black. Specific bright red can be seen in attached company logo.

Website needs to be modern, clean and professional representing our premium colocation and fibre provider branding.

Our company slogan is : safe. secure. reliable

We will provide feedback regardless of the quality of the design to ensure a better outcome for all parties.

Please feel free to contact us if you have any questions.

# The designer can use placeholder images or feel free to use any/all or none of the attached images
# The designer can use sample filler text

Target Market(s)

Technical IT Professionals as well C level executives (i.e. CEO's, CIO).

Industry/Entity Type

Internet

Requirements
Must have
• clean design
Nice to have
• A sidebar with two sections. 1 for current promo and 1 for "Let us call you back/contact you"
Should not have
• Clutter

```html
<!DOCTYPE html>
<html lang="en">
<head>
<meta charset="utf-8">
<title>Corvan Lk – Safe, Secure &amp; Reliable Data Centre</title>
<link rel="stylesheet" href="https://fonts.googleapis.com/css2?family=Arimo:wght@400;700&family=PT+Sans:wght@700&display=swap">
<style>
:root{
  --red:#d8262b;
  --rose:#c9777a;
  --rose-dark:#a9484c;
  --black:#000;
  --white:#fff;
  --grey-band:#ececec;
  --grey-card:#d4d4d4;
  --grey-text:#555;
  --ink:#111;
  --field:#bbb;
}
*{margin:0;padding:0;box-sizing:border-box}
html,body{width:694px;height:1200px;overflow:hidden}
body{position:relative;background:var(--white);font-family:"Arimo",Arial,sans-serif;color:var(--ink)}
.abs{position:absolute}

/* header */
.site-header{left:0;top:0;width:694px;height:92px;background:var(--black)}
.brand{left:20px;top:50px;display:flex;align-items:center;gap:7px;color:var(--white);font-size:22px;font-weight:700}
.brand-mark{width:14px;height:14px;background:var(--red)}
.phone{right:20px;top:16px;display:flex;align-items:center;gap:6px;color:var(--white);font-size:17px;font-style:italic;letter-spacing:1px}
.main-nav{right:10px;top:62px;display:flex;gap:13px;align-items:center}
.main-nav a{color:var(--white);font-size:9.5px;font-weight:700;text-decoration:none}
.main-nav a.is-active{background:var(--white);color:var(--rose);padding:3px 10px;border-radius:9px}

/* hero */
.hero{left:16px;top:91px;width:666px;height:323px;background:linear-gradient(#f4f4f4,#fdfdfd);border-radius:6px;overflow:hidden;box-shadow:0 1px 3px rgba(0,0,0,.25)}
.hero-photo{position:absolute;left:240px;top:0;width:426px;height:323px;background:linear-gradient(100deg,rgba(245,245,245,0) 0%,#e9d3c7 35%,#d4363a 60%,#b8262a 100%)}
.hero-title{position:absolute;left:14px;top:48px;font-family:"PT Sans",sans-serif;font-size:38px;color:#c98a8c;text-shadow:1px 1px 0 #7a4a4b,2px 2px 3px rgba(0,0,0,.3)}
.hero-sub{position:absolute;left:18px;top:92px;width:440px;font-size:16px;font-weight:700;line-height:21px;color:#111}
.btn{display:inline-block;background:linear-gradient(#e06a6e,var(--rose-dark));color:var(--white);font-weight:700;border-radius:4px;text-decoration:none;text-align:center}
.hero .btn{position:absolute;left:16px;top:135px;width:68px;height:20px;line-height:20px;font-size:10.5px;box-shadow:0 0 0 2px #eee}
.slider-ctrl{left:577px;top:352px;width:113px;height:34px;background:var(--red);border-radius:6px 0 0 6px;display:flex;align-items:center;padding-left:11px;gap:3px}
.slider-ctrl i{width:9px;height:9px;border-radius:50%;background:#f3a07a}
.slider-ctrl i.on{background:#111}
.slider-ctrl span{margin-left:16px;color:var(--white);font-size:9.5px;font-weight:700}

/* feature band */
.feature-band{left:16px;top:421px;width:666px;height:237px;background:var(--grey-band);border-radius:4px}
.feature{top:432px;width:170px}
.feature-tab{position:absolute;left:-10px;top:0;width:168px;height:27px;background:var(--white);box-shadow:0 2px 3px rgba(0,0,0,.35);font-size:15px;font-weight:700;text-align:center;line-height:27px}
.feature-card{position:absolute;left:0;top:27px;width:148px;height:180px;background:var(--grey-card);box-shadow:1px 1px 3px rgba(0,0,0,.3);padding:9px 7px;font-size:8.3px;line-height:16.5px;color:var(--grey-text)}
.feature-card strong{display:block;margin-top:12px;color:#444}
.feature .btn{position:absolute;left:86px;top:199px;width:56px;height:16px;line-height:16px;font-size:8.5px}
.badge{display:inline-block;background:#c4c4c4;border-radius:3px}

/* content */
.content{left:19px;top:672px;width:425px;font-size:8.5px;line-height:10px}
.content h2{font-size:19px;font-weight:400;margin-bottom:6px}
.content p{margin:0 0 10px 6px}
.content h3{font-size:9.5px;font-weight:400;margin:6px 0 2px 6px}
.content ul{list-style:none;margin-left:14px}
.content ul li:before{content:"•  "}
.more{color:var(--red);font-size:8.5px;display:block;margin:2px 0 8px 14px}
.fac-drawing{left:323px;top:932px;width:115px;height:113px;background:linear-gradient(135deg,#e5e5e5,#c6ccd8 50%,#e0b94a 70%,#d8d8d8);border-radius:6px}
.partner-mark{left:392px;top:838px;width:38px;height:27px;background:var(--red);border-radius:3px}
.divider{left:475px;top:675px;height:462px;border-left:1px dotted #888}

/* sidebar */
.sidebar{left:501px;top:670px;width:148px}
.sidebar h2{font-size:18px;font-weight:400;text-align:center;margin-bottom:8px}
.field{height:17px;border:1px solid var(--field);margin-bottom:7px;font-size:8px;color:#aaa;padding:3px 5px;position:relative}
.field.area{height:74px}
.field .drop{position:absolute;right:-1px;top:-1px;width:20px;height:17px;background:#9d5a5c}
.sb-btn{height:16px;line-height:16px;font-size:8px;padding:0 7px}
.sidebar-promo{left:504px;top:1009px;width:147px;height:121px;background:var(--rose);border-radius:7px;color:var(--white);font-size:8.3px;line-height:10px;padding:76px 7px 0}
.sidebar-promo .badge{position:absolute;left:14px;top:10px;width:118px;height:46px;background:#e9c0c1}

/* footer */
.site-footer{left:0;top:1145px;width:694px;height:55px;background:var(--black)}
.footer-sheet{left:16px;top:1137px;width:666px;height:22px;background:var(--white);border-radius:0 0 6px 6px}
.footer-nav{left:22px;top:1176px;color:var(--white);font-size:8.5px;font-weight:700}
.copyright{right:20px;top:1175px;color:var(--white);font-size:8.5px;font-weight:700}
</style>
</head>
<body>

<header class="abs site-header"></header>
<div class="abs brand"><span class="brand-mark"></span>Corvan Lk</div>
<div class="abs phone">
  <svg width="26" height="22" viewBox="0 0 26 22" aria-hidden="true"><path d="M3 8c0-4 20-4 20 0l-4 2-2-3H9L7 10z" fill="#3a7bd5"/><rect x="6" y="11" width="14" height="9" rx="2" fill="#3a7bd5"/><circle cx="13" cy="15.5" r="2.5" fill="#fff"/></svg>
  +61 8 5550 1420
</div>
<nav class="abs main-nav">
  <a class="is-active" href="#">HOME</a><a href="#">About Us</a><a href="#">Facilities</a><a href="#">Business Continuity</a><a href="#">Services</a><a href="#">Partners</a><a href="#">Webmail</a><a href="#">Contact Us</a>
</nav>

<section class="abs hero">
  <div class="hero-photo" role="img" aria-label="Photo of a smiling woman in a red top working on a laptop"></div>
  <h1 class="hero-title">Safe, Secure &amp; Reliable</h1>
  <p class="hero-sub">Corvan Lk's Safe, Secure &amp; Reliable Data Centre"Talk to us about designing a solution to meet your needs.</p>
  <a class="btn" href="#">Read More</a>
</section>
<div class="abs slider-ctrl"><i></i><i></i><i></i><i class="on"></i><span>Play</span></div>

<div class="abs feature-band"></div>
<section class="abs feature" style="left:41px">
  <h2 class="feature-tab">Business Continuity</h2>
  <div class="feature-card">No matter how safe and secure you feel right now, the stability of your entire organisation could be under serious threat! Whether a natural disaster such as fire or flood, or man made issue such as arson or theft, these disasters could cause untold damage to your IT infrastructure.</div>
  <a class="btn" href="#">Read More</a>
</section>
<section class="abs feature" style="left:276px">
  <h2 class="feature-tab">Corvan Lk Services</h2>
  <div class="feature-card">Corvan Lk currently offers colocation services with unsurpassed reliability and speed to hundreds of Australian based and international clients.<strong>Innovative IT Solutions...</strong></div>
  <a class="btn" href="#">Read More</a>
</section>
<section class="abs feature" style="left:510px">
  <h2 class="feature-tab">Partners</h2>
  <div class="feature-card">Corvan Lk is proud to partner with many of Australia's leading companies.
    <div style="margin-top:8px"><span class="badge" style="width:62px;height:22px"></span><span class="badge" style="width:38px;height:26px;margin-left:14px;border-radius:50%"></span></div>
    <div style="margin:12px 0 0 36px"><span class="badge" style="width:76px;height:30px"></span></div>
  </div>
  <a class="btn" href="#">Read More</a>
</section>

<main class="abs content">
  <h2>Welcome To&nbsp; Corvan Lk</h2>
  <p>A world class data centre in the safest place on Earth.</p>
  <p>With a centrally located data centre in the heart of the Perth CBD Corvan Lk is excellently positioned to assist with your critical IT requirements.</p>
  <p>The CBD facility features overlapping power grids, redundant power supplies and comprehensively maintained infrastructure, providing excellent levels of protection for your critical IT equipment. The State's newest and most technologically advanced data centre is also now open in Belmont, a convenient 5.5 km's from the CBD providing a perfect location for either production sites, or DR infrastructure.</p>
  <p>From Government departments to large corporations to SME's, Corvan Lk is the ideal company to assist with your colocation requirements. With warm racks already provisioned, you can begin using the data centre almost immediately.</p>
  <p>Call us today to see how we can help meet your needs.</p>
  <h2 style="margin-top:18px">Corvan Lk Facilities</h2>
  <p style="margin-left:14px">Corvan Lk maintains a world class data centre in the heart of the Perth CBD. With redundancy for all environmentals, you can rest assured your equipment is running in the optimal environment.</p>
  <h3>Facility Overview</h3>
  <ul><li>277.70sq m of computer room space;</li><li>138 x 42RU racks in main computer room (lockable);</li><li>Private high security cages available in 10 - 20 rack configurations;</li></ul>
  <a class="more" href="#">Read More</a>
  <h3>Nexor Network Hardware</h3>
  <ul><li>Stratus 6500 Switches with failover;</li><li>Stratus 6500 Firewall Module with failover;</li><li>5300 Access Servers;</li></ul>
  <a class="more" href="#">Read More</a>
</main>
<div class="abs partner-mark"></div>
<div class="abs fac-drawing" role="img" aria-label="Isometric floor plan illustration of the data centre computer room"></div>
<div class="abs divider"></div>

<aside class="abs sidebar">
  <h2>Corvan Lk WebMail</h2>
  <div class="field">Account Name ....</div>
  <div class="field">Account Password ....</div>
  <div class="field">POP3 Server ....<span class="drop"></span></div>
  <div style="text-align:right;margin-bottom:14px"><a class="btn sb-btn" href="#">Check Mail Now</a></div>
  <h2>Contact Us</h2>
  <div class="field">Name ....</div>
  <div class="field">Email Address ....</div>
  <div class="field">Subject ....</div>
  <div class="field area">Message ....</div>
  <div style="text-align:right"><a class="btn sb-btn" href="#">Send</a> &nbsp;<a class="btn sb-btn" href="#">Clear</a></div>
</aside>
<div class="abs sidebar-promo"><span class="badge"></span>Corvan Lk partners with Australia's leading providers of IT solutions and infrastructure.</div>

<footer class="abs site-footer"></footer>
<div class="abs footer-sheet"></div>
<div class="abs footer-nav">Home | About Us | Facilities | Business Continuity | Services | Partners | Webmail | Contact Us</div>
<div class="abs copyright">Copyright @ 2010 Corvan Lk&nbsp; All Rights Reserved</div>

</body>
</html>
```